Talvin Crestline Homes needs a business card

We need a business card for a new company in Canada, Ontario. Our company is all about luxury contraction homes for our clients. Our product and services are custom projects design. Under the business logo that will be created, we want a slogan that will be a memorable phrase for consumers to remember us to tell their friends and relatives.

Additional infomation
- Brennick Solvadeu
- President / Ceo
-415.390.7628

Find point what luxury construction products and services can be done

We like to see colors:
- #663300
- and something other colors or color that would attract the client needs and wants

The final design should communicate leads from new or old clients that will grow our empire. Most of all, we try to work among the budget that clients want

NOTE
- we also need an icon for the business (Example: Pictoloop, Friendvane, and Chattorq icons)
- We want the company name to be remembered easily for clients and our distributors who would get our orders.
- we need an icon on the business cards: Friendvane and Pictoloop.

Thanks,
Talvin Crestline Homes

```html
<!DOCTYPE html>
<html lang="en">
<head>
<meta charset="utf-8">
<title>Talvin Crestline Homes – Business Card</title>
<link href="https://fonts.googleapis.com/css2?family=Work+Sans:wght@400;600;700&display=swap" rel="stylesheet">
<style>
  :root {
    --stage: #262626;
    --card-brown: #663300;
    --card-brown-light: #72431f;
    --ink-light: #ffffff;
    --ink-deep: #4a2508;
    --rule: rgba(255,255,255,0.75);
  }
  * { box-sizing: border-box; margin: 0; padding: 0; }
  html, body {
    width: 1200px; height: 900px; overflow: hidden;
    background: var(--stage);
    font-family: "Work Sans", sans-serif;
  }
  .stage {
    position: relative; width: 1200px; height: 900px;
  }
  .card {
    position: absolute; left: 260px; width: 680px; height: 388px;
    background: linear-gradient(135deg, var(--card-brown) 0%, var(--card-brown-light) 100%);
    box-shadow: 0 12px 30px rgba(0,0,0,0.5);
  }
  .card--front { top: 46px; }
  .card--back { top: 466px; background: linear-gradient(160deg, var(--card-brown) 0%, #6a3814 100%); }

  .brand { text-align: center; }
  .brand__name { font-weight: 700; letter-spacing: 0.5px; }
  .brand__tagline { font-weight: 600; text-transform: uppercase; letter-spacing: 0.6px; }

  .card--front .brand {
    position: absolute; left: 0; right: 0; top: 142px; color: var(--ink-deep);
  }
  .card--front .brand__name { font-size: 42px; }
  .card--front .brand__tagline { font-size: 14.5px; margin-top: 6px; }

  .card--back .brand {
    position: absolute; right: 36px; top: 40px; color: var(--ink-light);
  }
  .card--back .brand__name { font-size: 27px; }
  .card--back .brand__tagline { font-size: 9.5px; margin-top: 3px; }

  .person { position: absolute; left: 48px; top: 212px; color: var(--ink-light); }
  .person__name { font-size: 23px; font-weight: 600; }
  .person__role { font-size: 17px; font-weight: 400; letter-spacing: 0.6px; margin-top: 2px; }

  .divider {
    position: absolute; left: 48px; right: 48px; top: 286px;
    border-top: 1px solid var(--rule);
  }
  .contact {
    position: absolute; left: 48px; right: 36px; top: 302px;
    color: var(--ink-light); font-size: 15.5px; letter-spacing: 0.4px; line-height: 1.75;
  }
</style>
</head>
<body>
<main class="stage">
  <section class="card card--front" aria-label="Card front">
    <div class="brand">
      <p class="brand__name">Talvin Crestline Homes</p>
      <p class="brand__tagline">- Home Renovations - Custom Project Design -</p>
    </div>
  </section>

  <section class="card card--back" aria-label="Card back">
    <div class="brand">
      <p class="brand__name">Talvin Crestline Homes</p>
      <p class="brand__tagline">- Home Renovations - Custom Project Design -</p>
    </div>
    <div class="person">
      <p class="person__name">Brennick Solvadeu</p>
      <p class="person__role">President / Ceo</p>
    </div>
    <div class="divider"></div>
    <div class="contact">
      <p>P : 415.390.7628 | E : info@talvincrestline.com | W : www.talvincrestline.com</p>
      <p>A : 2817 Marlow Avenue Kestrel, ON 40518</p>
    </div>
  </section>
</main>
</body>
</html>
```